SKVC Stationary and business Card
SKVC letterhead and Business Card
Professional
Summit Kinship Vitality Center
Dr. Marcus Pellham, D.C. Dr. Tamsin Pellham, D.C.
2948 Arden Avenue Boulder, CO 80304
drpellham@summitvitalityclinics.com
www.summitvitalityclinics.com

```html
<!DOCTYPE html>
<html lang="en">
<head>
<meta charset="utf-8">
<title>SKVC Stationery and Business Cards</title>
<link href="https://fonts.googleapis.com/css2?family=Cinzel:wght@400;600&family=Lato:wght@300;400&display=swap" rel="stylesheet">
<style>
:root{
  --purple:#6b4a9b;
  --purple-deep:#4e3278;
  --lilac:#b7a3d3;
  --mist:#ece7f3;
  --paper:#ffffff;
  --ink:#4a4a55;
  --ground:#e9e4dc;
}
*{box-sizing:border-box;margin:0;padding:0}
html,body{width:1200px;height:317px;overflow:hidden;background:var(--ground)}
.board{position:relative;width:1200px;height:317px;font-family:"Lato",sans-serif;color:var(--ink)}
.piece{position:absolute;background:var(--paper);box-shadow:0 1px 3px rgba(0,0,0,.18);overflow:hidden}
.caption{position:absolute;font-size:5px;letter-spacing:.5px;text-transform:uppercase;color:#8a8378;text-align:center}
.swoosh{position:absolute;left:0;top:0;width:100%;height:100%}
.brand{position:absolute;display:flex;align-items:center;gap:3px;font-family:"Cinzel",serif;color:var(--purple);white-space:nowrap}
.brand .dot{border-radius:50%;background:var(--purple);flex:none}
.brand small{display:block;font-family:"Lato",sans-serif;font-size:.5em;letter-spacing:.6px;color:var(--lilac)}
.emblem-faint{position:absolute;border-radius:50%;background:var(--mist)}
.fine{position:absolute;font-size:3.5px;line-height:1.5;color:var(--ink)}
.card{width:86px;height:48px}
.card.reverse{background:var(--purple)}
.card.reverse .brand{color:#fff}
.card.reverse .brand .dot{background:#fff}
.letterhead{width:185px;height:266px;top:17px}
.envelope{width:259px;height:96px}
.flap{position:absolute;left:0;top:0;width:100%;height:100%}
</style>
</head>
<body>
<main class="board">

  <p class="caption" style="left:17px;top:78px;width:200px;text-align:left">Business Card Designs</p>

  <!-- Business card A front -->
  <section class="piece card" style="left:17px;top:91px">
    <svg class="swoosh" viewBox="0 0 86 48" preserveAspectRatio="none"><path d="M0 0H40C22 10 10 28 6 48H0Z" fill="var(--purple)"/><path d="M40 0C26 10 14 28 10 48H6C10 28 22 10 40 0Z" fill="var(--lilac)"/></svg>
    <div class="brand" style="left:18px;top:8px;font-size:5px"><span class="dot" style="width:5px;height:5px"></span><span>Summit Kinship<small>Vitality Center</small></span></div>
    <p class="fine" style="left:40px;top:26px;font-size:2.6px">Dr. Marcus Pellham, D.C.<br>2948 Arden Avenue<br>Boulder, CO 80304<br>www.summitvitalityclinics.com</p>
  </section>
  <!-- Business card A back -->
  <section class="piece card reverse" style="left:115px;top:91px">
    <div class="brand" style="left:16px;top:18px;font-size:6px"><span class="dot" style="width:6px;height:6px"></span><span>Summit Kinship<small>Vitality Center</small></span></div>
  </section>
  <p class="caption" style="left:17px;top:141px;width:86px">Card Front A</p>
  <p class="caption" style="left:115px;top:141px;width:86px">Card Back A</p>

  <!-- Business card B front -->
  <section class="piece card" style="left:17px;top:149px">
    <svg class="swoosh" viewBox="0 0 86 48" preserveAspectRatio="none"><path d="M0 48H50C30 40 12 24 6 0H0Z" fill="var(--purple)"/></svg>
    <div class="brand" style="left:30px;top:8px;font-size:5px"><span class="dot" style="width:5px;height:5px"></span><span>Summit Kinship<small>Vitality Center</small></span></div>
    <p class="fine" style="left:44px;top:26px;font-size:2.6px">Dr. Tamsin Pellham, D.C.<br>drpellham@summitvitalityclinics.com</p>
  </section>
  <!-- Business card B back -->
  <section class="piece card reverse" style="left:115px;top:149px">
    <div class="emblem-faint" style="left:33px;top:14px;width:20px;height:20px;background:rgba(255,255,255,.85)"></div>
  </section>
  <p class="caption" style="left:17px;top:199px;width:86px">Card Front B</p>
  <p class="caption" style="left:115px;top:199px;width:86px">Card Back B</p>

  <!-- Letterhead page one -->
  <section class="piece letterhead" style="left:233px">
    <svg class="swoosh" viewBox="0 0 185 266" preserveAspectRatio="none"><path d="M0 0H34C16 60 8 160 14 266H0Z" fill="var(--purple)"/><path d="M34 0C18 60 12 160 20 266H16C8 160 16 60 30 0Z" fill="var(--lilac)"/></svg>
    <div class="brand" style="left:36px;top:10px;font-size:9px"><span class="dot" style="width:8px;height:8px"></span><span>Summit Kinship<small>Vitality Center</small></span></div>
    <p class="fine" style="left:112px;top:14px;font-size:3px;color:var(--lilac);text-align:right">2948 Arden Avenue · Boulder, CO 80304<br>www.summitvitalityclinics.com</p>
    <div class="emblem-faint" role="img" aria-label="Faint brand emblem" style="left:118px;top:170px;width:56px;height:56px"></div>
  </section>
  <p class="caption" style="left:233px;top:288px;width:185px">Letterhead Page One</p>

  <!-- Letterhead page two -->
  <section class="piece letterhead" style="left:437px">
    <svg class="swoosh" viewBox="0 0 185 266" preserveAspectRatio="none"><path d="M0 0H34C16 60 8 160 14 266H0Z" fill="var(--purple)"/><path d="M34 0C18 60 12 160 20 266H16C8 160 16 60 30 0Z" fill="var(--lilac)"/></svg>
    <div class="emblem-faint" role="img" aria-label="Faint brand emblem" style="left:60px;top:70px;width:90px;height:90px"></div>
  </section>
  <p class="caption" style="left:437px;top:288px;width:185px">Letterhead Page Two</p>

  <!-- Envelope front -->
  <section class="piece envelope" style="left:648px;top:139px">
    <div class="brand" style="left:10px;top:10px;font-size:8px"><span class="dot" style="width:7px;height:7px"></span><span>Summit Kinship<small>Vitality Center</small></span></div>
    <p class="fine" style="left:12px;top:34px;font-size:3px;color:var(--lilac)">2948 Arden Avenue · Boulder, CO 80304</p>
  </section>
  <p class="caption" style="left:648px;top:240px;width:259px">Envelope Front</p>

  <!-- Envelope back -->
  <section class="piece envelope" style="left:924px;top:139px">
    <svg class="flap" viewBox="0 0 259 96" preserveAspectRatio="none"><path d="M0 0H259V28C200 48 160 50 129 50S58 48 0 28Z" fill="var(--purple)"/><path d="M0 28C58 48 98 50 129 50S200 48 259 28V31C200 51 160 53 129 53S58 51 0 31Z" fill="var(--lilac)"/></svg>
    <div class="emblem-faint" style="left:124px;top:64px;width:10px;height:10px;background:var(--purple)"></div>
  </section>
  <p class="caption" style="left:924px;top:240px;width:259px">Envelope Back View</p>

</main>
</body>
</html>
```